Freelance IT consultant - minimalist website

I am an independent IT consultant / contractor with established clients. In many cases I sub-contract through other IT companies when performing work for external clients, in which case I am obliged to adopt these other companies' corporate branding. However I am becoming aware that my personal inclusion / involvement is adding significant value to these 3rd party companies' offerings, making them more attractive to their clients. I would like to capitalise on that value by developing my own "personal brand" - providing a means of distinguishing myself from other companies through whom I sub-contract. I figure a personal website would be a good place to start!

I want a design which evokes concepts of "smart, sensible solutions"; "clean and concise". My "competitors" have a tendency towards jargon, and verbose, often meaningless prose. I would like to position myself as the "go to man" for the solution - pure and simple - once all of the posturing and postulating has been finished. (NB: I've used the tagline "Solutions - Pure and Simple" for this project, but I'm receptive to other suggestions!)

Finally (...do you believe that? :-) ) my particular forte is Geographic Information Systems (GIS) and spatial databases. So if a website design can somehow incorporate the idea of maps, or the globe, that'd be brilliant (but keep this subtle - I'm not a cartographer and don't wish to convey that suggestion.) Something that suggests the connection between information and databases with maps and locations, perhaps?

Examples / concepts I like:
"Solution" - this is what I do! Often to ill-described, uncertain problems.
http://brevokhub.org/wp-content/uploads/2013/11/Solution.jpg
http://www.quorvanlabs.com.au/Media/Picture/Solutions.jpg

"Elegant design" - this is what I (like to think I) do :-)
http://pwwtrindle.files.blogvane.com/2013/03/nautilus1.png
http://static.pixelmoor.com/static/71d309ccf5c162d73102b4ec/t/71d357adf5c11c64d75c9899/2465010548160/Nautilus_Shell.png?format=1000w
Updates

I've added a PDF file with some unstructured thoughts and ideas around what I'm after. I realise I've left this brief quite open-ended - I don't mean to make it difficult. I'm really after some graphic design creative brilliance, more than website technical brilliance. Hope this helps!

I've uploaded an excerpt from my personal CV in a bid to answer some of the ... well, quite reasonable questions I'm receiving about what the hell it is that I actually do! By way of explanation, I didn't upload this information - or indeed, by entire CV - originally, because I really am seeking something more timeless than a "latest CV." As I've indicated, I'm really trying to create a web presence to confirm my right to "be here". I fully expect that any serious customers who visit my site will follow through with a "contact me" action, at which time I will be able to respond with a discussion and/or CV tailored to a particular project. That's what I do. As for the not-so-serious visitors to my site, I'd like them to leave with an affirming nod and the mental note that, they've stumbled upon somebody credible. And if they bookmark the site, all the better! :-) Hope this helps!

Reason: I'd really like a couple of extra days to run these ideas past some friends and colleagues. This is great stuff - but like so many deadlines, this one snuck up a bit quicker than I was expecting!

Target Market(s)

Prospective clients already aware of my existence, seeking confirmation / reassurance of my bona-fides and relevance. Typically government or mainstream business IT procurement staff.

Industry/Entity Type

Contractor

Requirements
Must have
• Simple, clean, timeless (?) design. I want a stable, solid web "presence" but don't expect to have to "work" the site at all. It's a brochure, really. But that doesn't mean it can't be a good one!
Nice to have
• Incorporate new logo (currently subject of a separate ArtFlock project - no: 482917)
Single page design - (I could be persuaded otherwise, but can't see the need for more than one really!)
Should not have
• Rolling banners, smiling actors / actresses, etc (I have no interest in updating these images!)
Shopping cart, news feeds, blah, blah... This is a static advertising presence only.

```html
<!DOCTYPE html>
<html lang="en">
<head>
<meta charset="utf-8">
<title>Northquill Consulting | IT Consultant</title>
<link rel="stylesheet" href="https://fonts.googleapis.com/css2?family=Ubuntu:wght@300;400;500&display=swap">
<style>
:root{
  --blue:#1a6fc0;
  --ink:#2b2b2b;
  --text:#555;
  --muted:#8a8a8a;
  --line:#1a6fc0;
  --field:#f4f4f4;
  --white:#fff;
  --feature-text:#d7e6f6;
}
*{box-sizing:border-box;margin:0;padding:0}
html,body{width:1200px;height:3418px;overflow:hidden}
body{position:relative;background:var(--white);font-family:"Ubuntu",sans-serif;color:var(--text)}
.abs{position:absolute}
svg{display:block}

/* hero */
.hero{left:0;top:0;width:1200px;height:940px;background:linear-gradient(100deg,#fafafa 0%,#eef0f2 38%,#c9d2dc 62%,#8ea2bc 80%,#dfe3e8 100%)}
.brand{left:60px;top:0;width:156px;height:144px;background:var(--blue);color:var(--white);font-size:14px;font-weight:500;letter-spacing:1px;line-height:18px;padding:96px 10px 0 12px;text-transform:uppercase}
.topbar{top:26px;font-size:15px;color:var(--white);display:flex;align-items:center;gap:8px}
.nav{top:72px;left:750px;display:flex;font-size:13px;font-weight:500;color:var(--white);text-transform:uppercase}
.nav a{padding:12px 14px;height:38px}
.nav .active{background:var(--blue)}
.hero-title{left:60px;top:300px;color:var(--ink);font-weight:400;text-transform:uppercase;letter-spacing:2px}
.hero-title .kicker{display:block;font-size:44px;font-weight:300;line-height:48px}
.hero-title .main{display:block;font-size:72px;font-weight:400;line-height:76px;letter-spacing:2px}
.hero-lead{left:60px;top:442px;width:620px;font-size:14px;line-height:20px;color:#444}
.feature{top:677px;height:175px;background:var(--blue);color:var(--white);padding:40px 20px 0 30px;display:flex;gap:18px;opacity:.96}
.feature h3{font-size:23px;font-weight:400;margin:0 0 14px}
.feature p{font-size:13px;line-height:18px;color:var(--feature-text)}

/* sections */
.section-title{left:0;width:1200px;text-align:center;font-size:19px;letter-spacing:4px;color:var(--blue);text-transform:uppercase;font-weight:400}
.rule{left:510px;width:180px;height:2px;background:var(--line)}
.intro{left:330px;width:540px;text-align:center;font-size:15px;line-height:24px;color:var(--text)}
.service{width:330px;text-align:center}
.service h4{font-size:16px;font-weight:500;color:var(--ink);margin:24px 0 26px}
.service p{font-size:14px;line-height:22px}

.band{left:0;top:1522px;width:1200px;height:366px;background:radial-gradient(ellipse at 50% 50%,#3a8fe0 0%,#165fae 45%,#0a2f66 100%)}
.band-title{left:0;width:1200px;top:1645px;text-align:center;color:var(--white);font-size:34px;font-weight:400;letter-spacing:1px;text-transform:uppercase}
.band-sub{left:0;width:1200px;top:1708px;text-align:center;color:var(--white);font-size:19px}

.col{width:340px}
.col h3{font-size:25px;font-weight:400;color:var(--ink);margin-bottom:22px}
.col p{font-size:14px;line-height:22px}

.display{left:100px;top:2440px;width:1000px;height:280px;background:linear-gradient(180deg,#0b2c60 0%,#2c78d4 55%,#e4e6ea 80%,#ffffff 100%);border-radius:14px 14px 40px 40px}

.info li{list-style:none;display:flex;align-items:center;gap:12px;font-size:14px;margin-bottom:16px;color:var(--text)}
.info .link{color:var(--blue)}
.field{background:var(--field);font-size:13px;color:var(--muted);padding:12px 10px}
.submit{left:800px;top:3180px;width:342px;height:44px;background:var(--blue);color:var(--white);font-size:17px;letter-spacing:3px;text-align:center;line-height:44px;text-transform:uppercase}

.footer{left:0;top:3340px;width:1200px;height:78px;background:var(--blue)}
.footer-notch{left:550px;top:3312px}
.footer-text{left:0;width:1200px;top:3370px;text-align:center;color:var(--white);font-size:15px}
.footer-text strong{font-weight:500}
</style>
</head>
<body>

<div class="abs hero" role="img" aria-label="Photograph of a jigsaw-puzzle globe with loose puzzle pieces on a light surface"></div>
<div class="abs brand">Northquill<br>Consulting</div>

<div class="abs topbar" style="left:740px">
  <svg width="18" height="14" viewBox="0 0 18 14"><rect x="1" y="1" width="16" height="12" fill="none" stroke="#1a6fc0" stroke-width="2"/><path d="M1 1l8 7 8-7" fill="none" stroke="#1a6fc0" stroke-width="2"/></svg>
  contacts@northquill.net
</div>
<div class="abs topbar" style="left:1002px">
  <svg width="16" height="16" viewBox="0 0 16 16"><path d="M3 1l3 3-2 2c1 2 3 4 5 5l2-2 3 3-2 2C7 14 2 9 1 3z" fill="#1a6fc0"/></svg>
  (123) 555-0142
</div>

<nav class="abs nav">
  <a class="active">Home</a><a>Services</a><a>About us</a><a>Contact</a>
  <a><svg width="16" height="16" viewBox="0 0 16 16"><circle cx="6.5" cy="6.5" r="4.5" fill="none" stroke="#fff" stroke-width="2"/><path d="M10 10l4 4" stroke="#fff" stroke-width="2.4"/></svg></a>
</nav>

<h1 class="abs hero-title"><span class="kicker">Smart Solutions</span><span class="main">IT Consultant</span></h1>
<p class="abs hero-lead">Praesent faucibus nisl sit nulla sollicitudin a sed purus. Lorem Ipsum. Proin gravida nibh vel velit auctor. Aenean sollicitudin, lorem quis bibendum auctor.</p>

<div class="abs feature" style="left:50px;width:368px">
  <svg width="52" height="46" viewBox="0 0 52 46"><path d="M3 3h46v30H18l-10 9v-9H3z" fill="none" stroke="#fff" stroke-width="2"/><text x="26" y="26" fill="#fff" font-size="20" text-anchor="middle" font-family="Ubuntu,sans-serif">?</text></svg>
  <div><h3>Ask Me Anything</h3><p>Praesent faucibus nisl. Lorem Ipsum.<br>Proin gravida nibh vel velit auctor<br>aliquet.</p></div>
</div>
<div class="abs feature" style="left:422px;width:368px">
  <svg width="48" height="48" viewBox="0 0 48 48"><g fill="none" stroke="#fff" stroke-width="2"><circle cx="24" cy="24" r="21"/><ellipse cx="24" cy="24" rx="9" ry="21"/><path d="M3 24h42M7 13h34M7 35h34"/></g></svg>
  <div><h3>Brand &amp; Identity</h3><p>Praesent faucibus nisl. Lorem Ipsum.<br>Proin gravida nibh vel velit auctor<br>aliquet.</p></div>
</div>
<div class="abs feature" style="left:793px;width:355px">
  <svg width="56" height="46" viewBox="0 0 56 46"><g fill="none" stroke="#fff" stroke-width="2"><circle cx="20" cy="14" r="9"/><path d="M3 42c0-11 8-17 17-17s17 6 17 17z"/><circle cx="38" cy="12" r="7"/><path d="M36 23c9 0 17 5 17 15H40"/></g></svg>
  <div><h3>Adding Value</h3><p>Praesent faucibus nisl. Lorem Ipsum.<br>Proin gravida nibh vel velit auctor<br>aliquet.</p></div>
</div>

<!-- Services -->
<h2 class="abs section-title" style="top:1042px">Services</h2>
<div class="abs rule" style="top:1080px"></div>
<p class="abs intro" style="top:1106px">Lorem ipsum dolor sit amet, consectetur adipiscing elit. Maecenas ac augue at erat hendrerit dictum. Praesent porta, purus eget sagittis imperdiet.</p>

<div class="abs service" style="left:98px;top:1248px">
  <svg width="62" height="44" viewBox="0 0 62 44" style="margin:0 auto"><path d="M14 42a12 12 0 0 1-2-24 16 16 0 0 1 30-6 12 12 0 0 1 18 12 9 9 0 0 1-6 18z" fill="#1a6fc0"/></svg>
  <h4>IT Consultant / Contractor</h4>
  <p>Praesent faucibus nisl sit nulla sollicitudin a sed purus augue at erat hendrerit</p>
</div>
<div class="abs service" style="left:435px;top:1248px">
  <svg width="36" height="54" viewBox="0 0 36 54" style="margin:-6px auto 0"><path d="M18 2a16 16 0 0 0-16 16c0 12 16 34 16 34s16-22 16-34A16 16 0 0 0 18 2z" fill="#1a6fc0"/><circle cx="18" cy="18" r="6" fill="#fff"/></svg>
  <h4>Geographic Information Systems</h4>
  <p>voluptatem accusantium.Sed ut perspiciatis unde omnis augue at erat hendrerit</p>
</div>
<div class="abs service" style="left:770px;top:1244px">
  <svg width="46" height="56" viewBox="0 0 46 56" style="margin:0 auto -6px"><g fill="#1a6fc0"><ellipse cx="23" cy="8" rx="22" ry="7"/><path d="M1 13c0 4 10 7 22 7s22-3 22-7v10c0 4-10 7-22 7S1 27 1 23z"/><path d="M1 28c0 4 10 7 22 7s22-3 22-7v10c0 4-10 7-22 7S1 42 1 38z"/><path d="M1 43c0 4 10 7 22 7s22-3 22-7v5c0 4-10 7-22 7S1 52 1 48z"/></g></svg>
  <h4>Spatial Databases</h4>
  <p>Praesent faucibus nisl sit nulla sollicitudin a sed purus augue at erat hendrerit</p>
</div>

<!-- Enterprise band -->
<div class="abs band" role="img" aria-label="Photograph of a hand holding a glowing blue digital key"></div>
<h2 class="abs band-title">Enterprise Solutions</h2>
<p class="abs band-sub">Connectivity for organizations in need of constant communication.</p>

<!-- About -->
<h2 class="abs section-title" style="top:1986px">About Me</h2>
<div class="abs rule" style="top:2024px"></div>
<p class="abs intro" style="top:2052px">Lorem ipsum dolor sit amet, consectetur adipiscing elit. Maecenas ac augue at erat hendrerit dictum. Praesent porta, purus eget sagittis imperdiet.</p>

<div class="abs col" style="left:60px;top:2180px"><h3>My Vision</h3><p>His sumo verear torquatos et. Ad sint eripuit tractatos sit. Affert dissentiet nec ut. Eos no autem dolorem facilisi. Eu unum mucius scripserit qui. Ipsum omnes voluptaria est id.</p></div>
<div class="abs col" style="left:430px;top:2180px"><h3>My Mission</h3><p>In ius lorem consul ridens, corrumpit maiestatis scriptorem mei ex. Postulant dissentiunt id eum, sonet aliquid sensibus cum et. Ius tation argumentum et.</p></div>
<div class="abs col" style="left:800px;top:2180px"><h3>My Values</h3><p>Cum menandri urbanitas te, sea erat eligendi repudiandae cu, nam te nusquam sententiae cotidieque. Diam postea vulputate vis ne, usu vivendum accommodare ex</p></div>

<div class="abs display" role="img" aria-label="Widescreen display showing a glowing blue puzzle piece labelled Solution"></div>

<!-- Contact -->
<h2 class="abs section-title" style="top:2790px">Contact Us</h2>
<div class="abs rule" style="top:2828px"></div>
<p class="abs intro" style="top:2856px">Lorem ipsum dolor sit amet, consectetur adipiscing elit. Maecenas ac augue at erat hendrerit dictum. Praesent porta, purus eget sagittis imperdiet.</p>

<div class="abs col" style="left:60px;top:2960px"><h3>Visit Our Office</h3>
  <ul class="info">
    <li><svg width="14" height="18" viewBox="0 0 14 18"><path d="M7 1a6 6 0 0 0-6 6c0 5 6 10 6 10s6-5 6-10a6 6 0 0 0-6-6z" fill="#1a6fc0"/><circle cx="7" cy="7" r="2" fill="#fff"/></svg>Adress: 1234 Street Name, City Name</li>
    <li><svg width="16" height="16" viewBox="0 0 16 16"><path d="M3 1l3 3-2 2c1 2 3 4 5 5l2-2 3 3-2 2C7 14 2 9 1 3z" fill="#1a6fc0"/></svg>Phone: (123) 555-0142</li>
    <li><svg width="16" height="12" viewBox="0 0 16 12"><rect width="16" height="12" fill="#1a6fc0"/><path d="M0 0l8 7 8-7" fill="none" stroke="#fff" stroke-width="1.5"/></svg>Email: hireme@northquill.net</li>
  </ul>
</div>
<div class="abs col" style="left:430px;top:2960px"><h3>Business Hours</h3>
  <ul class="info">
    <li><svg width="16" height="16" viewBox="0 0 16 16"><circle cx="8" cy="8" r="7" fill="none" stroke="#1a6fc0" stroke-width="2"/><path d="M8 4v4h3" fill="none" stroke="#1a6fc0" stroke-width="2"/></svg>Mon. - Fri. 8am to 5pm</li>
    <li><svg width="16" height="16" viewBox="0 0 16 16"><circle cx="8" cy="8" r="7" fill="none" stroke="#1a6fc0" stroke-width="2"/><path d="M8 4v4h3" fill="none" stroke="#1a6fc0" stroke-width="2"/></svg>Sat. 8am to 11am</li>
    <li><svg width="16" height="16" viewBox="0 0 16 16"><circle cx="8" cy="8" r="7" fill="none" stroke="#1a6fc0" stroke-width="2"/><path d="M8 4v4h3" fill="none" stroke="#1a6fc0" stroke-width="2"/></svg>Sun. <span class="link">Don't Work</span></li>
  </ul>
</div>
<div class="abs col" style="left:800px;top:2960px"><h3>Visit Our Office</h3></div>
<div class="abs field" style="left:800px;top:3016px;width:162px;height:42px">Name</div>
<div class="abs field" style="left:972px;top:3016px;width:170px;height:42px">Email Id</div>
<div class="abs field" style="left:800px;top:3068px;width:342px;height:88px">Your Text</div>
<div class="abs submit">Submit</div>

<!-- Footer -->
<svg class="abs footer-notch" width="100" height="30" viewBox="0 0 100 30"><path d="M0 30L50 0l50 30z" fill="#1a6fc0"/></svg>
<div class="abs footer"></div>
<p class="abs footer-text">© 2014 <strong>Northquill Consulting</strong>. All rights reserved.</p>

</body>
</html>
```